Verdon Ridgeworks Ltd. - Refreshed business card challenge

A revised, refreshed business card design for my oil and gas company using my existing logo. Feel free to be as creative as you like!

Target Market(s)

bankers, lawyers

Industry/Entity Type

Oil And Gas Exploration

Contact Information for Business Card

See the "Must Haves" section

Font styles to use
Serif
Sans Serif

Colors

Designer to choose colors to be used in the design.

Requirements
Must have
• Existing business logo, name, title, email, phone number, business address
• Neil Hastow, CA, CPA
• Vice President Finance & Chief Financial Officer
• nhastow@verdonridgeworks.example
• office: (555)284-6071
• cell: (555)716-3342
• 840, 615 11 Street N.E.
• Calgary, AB
• X9Q 4K1
Should not have
• Should not be plain and boring.

```html
<!DOCTYPE html>
<html lang="en">
<head>
<meta charset="utf-8">
<title>Verdon Ridgeworks Ltd. – Business Card</title>
<link href="https://fonts.googleapis.com/css2?family=Arimo:wght@700&family=Open+Sans:wght@400&display=swap" rel="stylesheet">
<style>
  :root {
    --bg: #ecedef;
    --card: #ffffff;
    --green: #0d5a3a;
    --brown: #5a2e12;
    --ink: #3c3c3c;
    --rule: #6b6b6b;
  }
  * { box-sizing: border-box; margin: 0; padding: 0; }
  html, body { width: 1200px; height: 895px; overflow: hidden; }
  body { background: var(--bg); position: relative; font-family: "Open Sans", Arial, sans-serif; }
  .card {
    position: absolute;
    width: 620px; height: 354px;
    background: var(--card);
    border-radius: 18px;
    box-shadow: 0 6px 18px rgba(0,0,0,0.18);
  }
  .card-front { left: 110px; top: 60px; }
  .card-back { left: 470px; top: 470px; }
  .brand {
    position: absolute;
    display: flex; align-items: center; gap: 10px;
    font-family: "Arimo", Arial, sans-serif;
    font-weight: 700;
    color: var(--green);
    line-height: 1.05;
  }
  .brand-dot { border-radius: 50%; background: var(--green); flex: none; }
  .card-front .brand { left: 50%; top: 50%; transform: translate(-50%, -50%); font-size: 40px; }
  .card-front .brand-dot { width: 34px; height: 34px; }
  .card-back .brand { left: 48px; top: 50%; transform: translateY(-50%); font-size: 28px; }
  .card-back .brand-dot { width: 24px; height: 24px; }
  .divider {
    position: absolute; left: 320px; top: 60px;
    width: 1px; height: 234px; background: var(--rule);
  }
  .details { position: absolute; left: 340px; top: 58px; right: 18px; color: var(--ink); }
  .person-name {
    font-family: "Arimo", Arial, sans-serif; font-weight: 700;
    color: var(--green); font-size: 22px; line-height: 1.15;
  }
  .person-title { font-size: 13px; line-height: 1.35; margin-top: 2px; }
  .address { font-size: 13px; line-height: 1.35; margin-top: 12px; }
  .contacts { list-style: none; margin-top: 12px; font-size: 12.5px; line-height: 1.55; }
  .contacts li { display: flex; align-items: center; gap: 8px; white-space: nowrap; }
  .contacts svg { width: 12px; height: 12px; flex: none; fill: var(--brown); }
</style>
</head>
<body>
  <section class="card card-front" aria-label="Card front">
    <div class="brand"><span class="brand-dot"></span><span>Verdon Ridgeworks</span></div>
  </section>

  <section class="card card-back" aria-label="Card back">
    <div class="brand"><span class="brand-dot"></span><span>Verdon<br>Ridgeworks</span></div>
    <div class="divider"></div>
    <div class="details">
      <p class="person-name">Neil Hastow, CA, CPA</p>
      <p class="person-title">Vice President Finance &amp;<br>Chief Financial Officer</p>
      <p class="address">840, 615 11 Street N.E.<br>Calgary, AB X9Q 4K1</p>
      <ul class="contacts">
        <li><svg viewBox="0 0 12 12"><path d="M2.5 0.8l2 2-1 1.4c.6 1.4 1.8 2.6 3.3 3.3l1.4-1 2 2-1.2 1.9C5.5 10.2 1.8 6.5 1 2z"/></svg>(555)284-6071</li>
        <li><svg viewBox="0 0 12 12"><rect x="3.5" y="0.5" width="5" height="11" rx="1"/></svg>(555)716-3342</li>
        <li><svg viewBox="0 0 12 12"><path d="M0.5 2.5h11v7h-11z M0.5 2.5l5.5 4 5.5-4" stroke="#fff" stroke-width="0.8"/></svg>nhastow@verdonridgeworks.example</li>
        <li><svg viewBox="0 0 12 12"><circle cx="6" cy="6" r="5.5"/><path d="M0.5 6h11M6 0.5v11" stroke="#fff" stroke-width="0.8"/></svg>www.ridgeworksgroup.example</li>
      </ul>
    </div>
  </section>
</body>
</html>
```